Business Card Design Project

Please create a custom business card for Loftwell Capital. The logo is attached to this brief.

Also, here is the link to the logo design project: http://jobs.briskmotif.com/job.aspx?id=462035

Questions can be posted on the Discussion Board.

```html
<!DOCTYPE html>
<html lang="en">
<head>
<meta charset="utf-8">
<title>Loftwell Capital – Business Cards</title>
<link href="https://fonts.googleapis.com/css2?family=Source+Sans+3:wght@400;600;700&display=swap" rel="stylesheet">
<style>
  :root {
    --backdrop: #4a3f39;
    --card: #1b1b1c;
    --card-edge: #0e0e0f;
    --silver: #9a9a9c;
    --white: #f4f4f4;
    --blue: #2f86c9;
    --muted: #d8d8d8;
    --rule: #8a8a8a;
  }
  * { box-sizing: border-box; margin: 0; padding: 0; }
  html, body { width: 1200px; height: 811px; overflow: hidden; }
  body {
    background: var(--backdrop);
    font-family: "Source Sans 3", sans-serif;
    position: relative;
  }
  .card {
    position: absolute;
    top: 257px;
    width: 520px;
    height: 297px;
    background: var(--card);
    border-radius: 3px;
    box-shadow: 0 10px 24px rgba(0,0,0,.45);
  }
  .card--front { left: 60px; }
  .card--back { left: 620px; }

  .front-name {
    position: absolute;
    inset: 0;
    display: flex;
    align-items: center;
    justify-content: center;
    color: var(--silver);
    font-weight: 600;
    font-size: 42px;
    letter-spacing: 4px;
    text-transform: uppercase;
    text-align: center;
    line-height: 1.05;
  }

  .brand {
    position: absolute;
    top: 48px;
    right: 40px;
    width: 300px;
    text-align: center;
    color: var(--white);
    font-weight: 600;
    font-size: 30px;
    letter-spacing: 3px;
    text-transform: uppercase;
    line-height: 1.1;
  }

  .person {
    position: absolute;
    top: 168px;
    left: 24px;
    width: 215px;
    text-align: right;
    color: var(--muted);
    font-size: 14px;
    line-height: 1.35;
  }
  .person__name {
    color: var(--blue);
    font-weight: 700;
    font-size: 22px;
    line-height: 1.2;
    margin-bottom: 3px;
  }

  .divider {
    position: absolute;
    top: 176px;
    left: 256px;
    width: 1px;
    height: 98px;
    background: var(--rule);
  }

  .contacts {
    position: absolute;
    top: 172px;
    left: 272px;
    list-style: none;
    color: var(--white);
    font-size: 15px;
    line-height: 20px;
  }
  .contacts li { display: flex; align-items: center; gap: 7px; }
  .contacts svg { width: 11px; height: 11px; fill: var(--blue); flex: none; }
</style>
</head>
<body>
  <section class="card card--front" aria-label="Card front">
    <div class="front-name">Loftwell<br>Capital</div>
  </section>

  <section class="card card--back" aria-label="Card back">
    <div class="brand">Loftwell<br>Capital</div>

    <div class="person">
      <div class="person__name">Daniel R. Hale</div>
      <div>Managing Member</div>
      <div>2217 Harbor Lane,</div>
      <div>Fresno, CA 93721</div>
    </div>

    <div class="divider"></div>

    <ul class="contacts">
      <li><svg viewBox="0 0 12 12"><path d="M2.5 1l2 2.5-1 1.2a7 7 0 0 0 3.8 3.8l1.2-1 2.5 2-1 1.5C5 11 1 7 1 2z"/></svg>(559) 410-2285</li>
      <li><svg viewBox="0 0 12 12"><path d="M3 1h5l2 2v8H3z M5 5h4v1H5z M5 7h4v1H5z"/></svg>(559) 410-2286</li>
      <li><svg viewBox="0 0 12 12"><path d="M3.5 0.5h5v11h-5z M4.5 1.5v8h3v-8z"/></svg>(559) 733-0914</li>
      <li><svg viewBox="0 0 12 12"><path d="M1 2.5h10v7H1z M1.5 3l4.5 3.5L10.5 3" /></svg>daniel@harborlanedev.com</li>
      <li><svg viewBox="0 0 12 12"><circle cx="6" cy="6" r="5.5"/></svg>www.harborlanedev.com</li>
    </ul>
  </section>
</body>
</html>
```